Concise,Good colour matching,Good looks design for "HERD SURE RAPID TEST FOR LIVESTOCK"

Product Positioning: Affordable test for Large Animals (Livestock/Veterinary Use)
Product Name: HERD SURE Rapid Test Kit (for large animals, e.g., cattle, horses, swine,Avian,sheep).

2. Packaging Requirements

A. Visual Design
Color Scheme:
Green/Blue/Orange/Yellow/Red/Gray/White(chose 2~4 colors)

Mandatory Info:
Brand logo ("HERD SURE")

Target Market(s)

Southeast Asia, Africa, Middle East, South America

Industry/Entity Type

Veterinary diagnostic for LIVESTOCK

Colors

Designer to choose colors to be used in the design.

Requirements
Nice to have
• Concise,Good colour matching,Good looks

```html
<!DOCTYPE html>
<html lang="en">
<head>
<meta charset="utf-8">
<title>HERD SURE Rapid Test – Packaging Dieline</title>
<link href="https://fonts.googleapis.com/css2?family=Oswald:wght@600&family=Open+Sans:wght@400;600;700&display=swap" rel="stylesheet">
<style>
  :root {
    --teal: #1a8fb3;
    --teal-soft: #3aa3c2;
    --orange: #f6aa2e;
    --ink: #1f1f1f;
    --paper: #ffffff;
    --backdrop: #eeeeee;
    --meadow-top: #dfe3d6;
    --meadow-mid: #a9b98c;
    --meadow-low: #5f7e3c;
  }
  * { box-sizing: border-box; margin: 0; padding: 0; }
  html, body { width: 803px; height: 1200px; overflow: hidden; }
  body {
    background: var(--backdrop);
    font-family: "Open Sans", Arial, sans-serif;
    color: var(--ink);
    position: relative;
  }
  .dieline {
    position: absolute;
    left: 10px; top: 420px;
    width: 783px; height: 359px;
  }
  .panel { position: absolute; overflow: hidden; }
  .panel-top {
    left: 251px; top: 0; width: 287px; height: 181px;
    background: var(--teal);
    display: flex; flex-direction: column; align-items: center; justify-content: center; gap: 12px;
  }
  .panel-left, .panel-right { background: var(--paper); top: 181px; height: 178px; }
  .panel-left { left: 0; width: 251px; }
  .panel-right { left: 538px; width: 245px; }
  .panel-front { left: 251px; top: 181px; width: 287px; height: 178px; }

  .brand { display: flex; align-items: center; gap: 6px; }
  .brand-dot { width: 20px; height: 20px; border-radius: 50%; border: 3px solid currentColor; }
  .brand-name { font-family: "Oswald", "Arial Narrow", sans-serif; font-weight: 600; font-size: 20px; letter-spacing: .5px; }
  .panel-top .brand { color: var(--paper); }
  .tagline {
    background: var(--paper); color: var(--ink);
    font-weight: 600; font-size: 10.5px;
    padding: 3px 10px; border-radius: 6px;
  }

  .meadow {
    position: absolute; inset: 0;
    background: linear-gradient(180deg, var(--meadow-top) 0%, #d3d9c5 35%, var(--meadow-mid) 62%, var(--meadow-low) 100%);
  }
  .front-head {
    position: relative; z-index: 1;
    display: flex; flex-direction: column; align-items: center; gap: 3px; padding-top: 14px;
  }
  .front-head .brand { color: #333; }
  .front-head .brand-dot { width: 13px; height: 13px; border-width: 2px; }
  .front-head .brand-name { font-size: 13px; }
  .front-tagline {
    background: var(--teal-soft); color: var(--paper);
    font-weight: 700; font-size: 10px;
    padding: 2px 10px; border-radius: 10px;
  }

  .side-header {
    display: flex; align-items: center; justify-content: center; gap: 5px;
    margin-top: 24px;
  }
  .end-cap { width: 18px; height: 13px; background: var(--teal); border-radius: 7px; }
  .side-header .brand { color: #333; }
  .side-header .brand-dot { width: 13px; height: 13px; border-width: 2px; }
  .side-header .brand-name { font-size: 12px; }
  .rapid-pill {
    background: var(--orange); color: var(--paper);
    font-family: "Oswald", "Arial Narrow", sans-serif; font-weight: 600; font-size: 10px;
    padding: 1px 7px; border-radius: 8px;
  }

  .side-body { display: flex; gap: 20px; padding: 20px 0 0 56px; }
  .panel-right .side-body { padding-left: 52px; gap: 18px; }
  .badges { display: flex; flex-direction: column; gap: 8px; width: 34px; align-items: center; }
  .badge { display: flex; flex-direction: column; align-items: center; gap: 2px; }
  .badge-mark { width: 19px; height: 19px; border-radius: 50%; display: flex; align-items: center; justify-content: center; }
  .badge-mark.teal { background: var(--teal); }
  .badge-mark.orange { background: var(--orange); }
  .badge-label { font-size: 4.5px; line-height: 1.2; text-align: center; width: 34px; }
  .copy { font-size: 6.3px; line-height: 1.35; width: 100px; padding-top: 6px; }
  .copy p + p { margin-top: 6px; }
  .copy strong { color: var(--teal); font-weight: 700; }
</style>
</head>
<body>
  <main class="dieline">
    <section class="panel panel-top">
      <div class="brand"><span class="brand-dot"></span><span class="brand-name">HERD SURE</span></div>
      <div class="tagline">Affordable Diagnostics for Healthy Herds</div>
    </section>

    <section class="panel panel-left">
      <div class="side-header">
        <span class="end-cap"></span>
        <div class="brand"><span class="brand-dot"></span><span class="brand-name">HERD SURE</span></div>
        <span class="rapid-pill">RAPID TEST</span>
        <span class="end-cap"></span>
      </div>
      <div class="side-body">
        <div class="badges">
          <div class="badge"><span class="badge-mark teal"></span><span class="badge-label">Large Animal</span></div>
          <div class="badge">
            <span class="badge-mark orange">
              <svg width="11" height="11" viewBox="0 0 12 12"><path d="M2.5 6.2l2.3 2.3 4.7-5" fill="none" stroke="#fff" stroke-width="1.6" stroke-linecap="round" stroke-linejoin="round"/></svg>
            </span>
            <span class="badge-label">Rapid Results in 10 Minutes</span>
          </div>
        </div>
        <div class="copy">
          <p>Manufactured by FIELDLAB</p>
          <p><strong>Storage:</strong> 2-30°C, Do not freeze<br>See the instructions for other contents</p>
        </div>
      </div>
    </section>

    <section class="panel panel-front">
      <div class="meadow" role="img" aria-label="Misty green pasture with grazing cows, sheep and geese beside a stream"></div>
      <div class="front-head">
        <div class="brand"><span class="brand-dot"></span><span class="brand-name">HERD SURE</span></div>
        <div class="front-tagline">Affordable Diagnostics for Healthy Herds</div>
      </div>
    </section>

    <section class="panel panel-right">
      <div class="side-header">
        <span class="end-cap"></span>
        <div class="brand"><span class="brand-dot"></span><span class="brand-name">HERD SURE</span></div>
        <span class="rapid-pill">RAPID TEST</span>
        <span class="end-cap"></span>
      </div>
      <div class="side-body">
        <div class="badges">
          <div class="badge"><span class="badge-mark teal"></span><span class="badge-label">Large Animal</span></div>
          <div class="badge">
            <span class="badge-mark orange">
              <svg width="11" height="11" viewBox="0 0 12 12"><path d="M2.5 6.2l2.3 2.3 4.7-5" fill="none" stroke="#fff" stroke-width="1.6" stroke-linecap="round" stroke-linejoin="round"/></svg>
            </span>
            <span class="badge-label">Rapid Results in 10 Minutes</span>
          </div>
        </div>
        <div class="copy">
          <p><strong>Affordable:</strong> Colloidal gold-based rapid tests that combine high accuracy with cost-effectiveness.</p>
          <p><strong>Reliable &amp; Simple:</strong> Stable test performance with 2-30°C, Easy to operate, no professional skills required.</p>
        </div>
      </div>
    </section>
  </main>
</body>
</html>
```